Business Bench-marking brochure

Create a single page flyer for an account firm to advertise their Business Bench-marking product offering.

Style should follow new corporate image in development as per attached website psd.

The client likes the logo to always be on the RIGHT of publications.

Target Market(s)

Small - Medium sucessfully Business

Industry/Entity Type

Business

Colors
eb1f27

Requirements
Nice to have
• The client would like an image of a scales with Apples on both sides to be used -the idea being "comparing apples to apples"

```html
<!DOCTYPE html>
<html lang="en">
<head>
<meta charset="utf-8">
<title>Kestrel Business Consulting – Benchmarking Flyer</title>
<link rel="stylesheet" href="https://fonts.googleapis.com/css2?family=Lato:wght@400;700&family=Roboto+Condensed:wght@700&display=swap">
<style>
  :root {
    --brand-red: #eb1f27;
    --deep-red: #b3141a;
    --ink: #2b2b2b;
    --paper: #ffffff;
    --night: #161616;
    --night-soft: #3a3a3a;
    --backdrop: #000000;
    --photo-light: #eef1f4;
    --photo-mid: #b9c6d3;
  }
  * { box-sizing: border-box; margin: 0; padding: 0; }
  html, body { width: 938px; height: 1200px; overflow: hidden; }
  body {
    position: relative;
    background: var(--backdrop);
    font-family: "Lato", Arial, sans-serif;
    color: var(--ink);
  }
  .condensed { font-family: "Roboto Condensed", "Arial Narrow", sans-serif; font-weight: 700; }

  .flyer {
    position: absolute; left: 55px; top: 62px; width: 830px; height: 1066px;
    background: linear-gradient(160deg, var(--brand-red), var(--deep-red));
  }

  /* top white panel */
  .intro-panel {
    position: absolute; left: 60px; top: 85px; width: 822px; height: 450px;
    background: var(--paper);
    clip-path: polygon(210px 0, 100% 0, 100% 100%, 0 100%, 0 36px, 180px 36px);
  }
  .intro-photo {
    position: absolute; left: 60px; top: 121px; width: 340px; height: 414px;
    background: linear-gradient(100deg, var(--photo-mid) 0%, var(--photo-light) 70%, var(--paper) 100%);
  }
  .brand {
    position: absolute; left: 420px; top: 106px;
    display: flex; align-items: center; gap: 14px;
  }
  .brand-name {
    font-family: "Lato", Arial, sans-serif; font-weight: 700;
    color: var(--ink); text-align: left; line-height: 1;
  }
  .brand-name .word { display: block; font-size: 46px; }
  .brand-name .line { display: block; font-size: 18px; margin-top: 6px; }
  .brand-mark { width: 56px; height: 56px; background: var(--brand-red); }

  .stack-up {
    position: absolute; left: 398px; top: 208px; width: 436px; height: 38px;
    background: var(--deep-red); border-radius: 10px;
    color: var(--paper); font-size: 28px; line-height: 38px; text-align: center;
  }
  .checklist { position: absolute; left: 398px; top: 262px; width: 432px; list-style: none; }
  .checklist li {
    position: relative; padding-left: 24px; font-size: 14.5px; line-height: 18px; margin-bottom: 20px;
  }
  .checklist svg { position: absolute; left: 0; top: 2px; }

  /* dark lower section */
  .detail-panel {
    position: absolute; left: 60px; top: 535px; width: 822px; height: 555px;
    background: radial-gradient(ellipse at 40% 35%, var(--night-soft), var(--night) 75%);
  }
  .performance-banner {
    position: absolute; left: 150px; top: 512px; width: 640px; height: 133px;
    background: linear-gradient(180deg, var(--brand-red), var(--deep-red));
    clip-path: polygon(0 0, 100% 0, 95% 100%, 5% 100%);
    color: var(--paper); text-align: center; padding-top: 6px;
  }
  .performance-banner .lead { font-size: 38px; line-height: 50px; }
  .performance-banner .punch { font-size: 62px; line-height: 66px; }

  .offer {
    position: absolute; left: 101px; top: 666px; width: 360px;
    color: var(--paper); font-size: 14.5px; line-height: 19.5px;
  }
  .offer p + p { margin-top: 19px; }
  .consultant-photo {
    position: absolute; left: 160px; top: 800px; width: 210px; height: 290px;
    background: linear-gradient(180deg, #4a4a4a, #121212);
    border-radius: 105px 105px 0 0;
  }

  .benefits { position: absolute; left: 472px; top: 670px; width: 380px; color: var(--paper); }
  .benefits h2 { color: var(--brand-red); font-size: 30px; line-height: 40px; margin-bottom: 20px; }
  .benefits ol { list-style: none; }
  .benefits li { font-size: 19.5px; line-height: 26px; margin-bottom: 24px; }
  .benefits li span { color: var(--brand-red); }

  .contact-band {
    position: absolute; left: 470px; top: 1042px; width: 412px; height: 48px;
    background: var(--brand-red);
    clip-path: polygon(40px 0, 100% 0, 100% 100%, 0 100%);
  }
  .contact {
    position: absolute; right: 90px; top: 1046px;
    color: var(--paper); font-size: 19px; line-height: 26px; text-align: right;
  }
  .contact .phone { display: inline-flex; align-items: center; gap: 22px; }
</style>
</head>
<body>
  <div class="flyer"></div>
  <div class="intro-panel"></div>
  <div class="intro-photo" role="img" aria-label="Photo of a man working on a laptop in a bright office"></div>

  <div class="brand">
    <div class="brand-name"><span class="word">KESTREL</span><span class="line">BUSINESS CONSULTING</span></div>
    <div class="brand-mark"></div>
  </div>

  <div class="stack-up condensed">Does your business stack up?</div>

  <ul class="checklist">
    <li><svg width="18" height="16" viewBox="0 0 18 16"><path d="M1 9l5 5L17 2" fill="none" stroke="#b3141a" stroke-width="3"/></svg>Ever wondered how your business compares to your competitors?</li>
    <li><svg width="18" height="16" viewBox="0 0 18 16"><path d="M1 9l5 5L17 2" fill="none" stroke="#b3141a" stroke-width="3"/></svg>Why you may be struggling to make a profit while other businesses in your industry seem to have it all figured out?</li>
    <li><svg width="18" height="16" viewBox="0 0 18 16"><path d="M1 9l5 5L17 2" fill="none" stroke="#b3141a" stroke-width="3"/></svg>By capturing the financial information and KPIs of your business we can compare your business to those within your industry. This enables you to be armed with the knowledge of how you can take corrective action by making informed decisions to save money and significantly enhance your overall performance</li>
  </ul>

  <div class="detail-panel"></div>

  <div class="performance-banner condensed">
    <div class="lead">Is your business performance</div>
    <div class="punch">good, bad or ugly?</div>
  </div>

  <div class="offer">
    <p>To ensure your business is operating at its peak performance, call Kestrel Business Consulting for your detailed benchmark report.</p>
    <p>Full analysis of your financial statements, including KPIs, along with a meeting with Dana Whitfield to identify areas to improve to help your business prosper.</p>
  </div>

  <div class="consultant-photo" role="img" aria-label="Photo of a smiling consultant in a dark suit with arms folded"></div>

  <div class="benefits">
    <h2 class="condensed">Benchmarking helps you:</h2>
    <ol>
      <li><span>1.</span> Identify where you can<br>reduce costs and improve efficiencies</li>
      <li><span>2.</span> Determine the productivity of<br>your employees</li>
      <li><span>3.</span> Highlight opportunities for<br>improvement and innovative practices</li>
      <li><span>4.</span> Discover opportunities for<br>making your business more competitive</li>
    </ol>
  </div>

  <div class="contact-band"></div>
  <div class="contact">
    <div>hello@kestrelconsulting.com.au</div>
    <div class="phone">
      <svg width="24" height="20" viewBox="0 0 26 22"><path d="M2 8c0-4 22-4 22 0v2h-6V7H8v3H2z" fill="#fff"/><path d="M6 11h14l3 9H3z" fill="#fff"/><circle cx="13" cy="15" r="3" fill="#eb1f27"/></svg>
      <span>02 5550 1842</span>
    </div>
  </div>
</body>
</html>
```